Velmora EIRL Business Card Design Project

We need a business card design for a New Business Intelligence Consultant. We bring a complete service to the client from first consulting meeting to help desk and system improvement.

I will upload the company logo and I like to use the logo colors on the card. Feel free to use all logo components on the design, for example one side with the black logo using complete card and the other side only the red shape (is an example, feel absolutely free :)).

The principal idea is to sell a professional service and a modern company.

Target Market(s)

IT Business Intelligence Clients

Industry/Entity Type

Professional Service

Requirements
Nice to have
• - Use the logo colors and minimize white sections.
- Rounded borders
Should not have
• I don't want to see any references to people working on a meeting or office photos or any computers related logos.

```html
<!DOCTYPE html>
<html lang="es">
<head>
<meta charset="utf-8">
<title>Velmora EIRL – Tarjetas de presentación</title>
<link rel="stylesheet" href="https://fonts.googleapis.com/css2?family=Open+Sans:wght@400;600;700&display=swap">
<style>
  :root {
    --bg: #efefef;
    --card: #2b2a29;
    --red: #e31e24;
    --grey: #a8a8a8;
    --grey-light: #bdbdbd;
    --text-soft: #c9c9c9;
  }
  * { margin: 0; padding: 0; box-sizing: border-box; }
  html, body { width: 1200px; height: 900px; overflow: hidden; }
  body {
    position: relative;
    background: var(--bg);
    font-family: "Open Sans", Arial, sans-serif;
  }
  .card {
    position: absolute;
    width: 532px;
    height: 294px;
    background: var(--card);
    border-radius: 16px;
    overflow: hidden;
  }
  .card--front { left: 137px; top: 125px; }
  .card--back  { left: 521px; top: 471px; }

  /* Front */
  .brand {
    position: absolute;
    left: 91px;
    top: 98px;
    display: flex;
    align-items: center;
    gap: 28px;
  }
  .brand__square {
    width: 64px;
    height: 64px;
    background: var(--grey);
  }
  .brand__name {
    font-size: 74px;
    font-weight: 600;
    line-height: 1;
    letter-spacing: -1px;
    color: var(--red);
  }
  .front-band {
    position: absolute;
    left: 0; right: 0; bottom: 0;
    height: 31px;
    background: var(--red);
    text-align: center;
    font-size: 17px;
    line-height: 31px;
    color: var(--grey-light);
  }

  /* Back */
  .back-accent {
    position: absolute;
    left: 40px;
    top: 72px;
    width: 150px;
    height: 150px;
    background: var(--red);
  }
  .person {
    position: absolute;
    left: 296px;
    top: 46px;
    width: 236px;
  }
  .person__name {
    font-size: 23px;
    font-weight: 700;
    color: var(--grey);
    line-height: 1.2;
  }
  .person__role {
    font-size: 18px;
    color: var(--grey);
    line-height: 1.35;
  }
  .person__rule {
    margin-top: 14px;
    height: 1px;
    background: var(--red);
  }
  .contact {
    position: absolute;
    left: 296px;
    top: 135px;
    list-style: none;
    font-size: 14px;
    line-height: 17.8px;
    color: var(--text-soft);
  }
  .contact li {
    display: flex;
    align-items: flex-start;
  }
  .contact svg {
    width: 10px;
    height: 10px;
    margin: 4px 8px 0 0;
    flex: none;
    fill: var(--grey-light);
  }
</style>
</head>
<body>

<section class="card card--front" aria-label="Frente de la tarjeta">
  <div class="brand">
    <span class="brand__square"></span>
    <span class="brand__name">velmora</span>
  </div>
  <div class="front-band">www.velmora.cl</div>
</section>

<section class="card card--back" aria-label="Reverso de la tarjeta">
  <div class="back-accent"></div>

  <div class="person">
    <h1 class="person__name">Tomás Herrera L.</h1>
    <p class="person__role">Gerente General</p>
    <div class="person__rule"></div>
  </div>

  <ul class="contact">
    <li>
      <svg viewBox="0 0 10 10"><path d="M2 0h2l1 3-1.4 1a6 6 0 0 0 2.4 2.4L7 5l3 1v2c0 1-1 2-2 2A8 8 0 0 1 0 2c0-1 1-2 2-2z"/></svg>
      <span>+56 (9) 84216390</span>
    </li>
    <li>
      <svg viewBox="0 0 10 10"><path d="M0 2h10v1L5 6 0 3zM0 4l5 3 5-3v4H0z"/></svg>
      <span>tomas@velmora.cl</span>
    </li>
    <li>
      <svg viewBox="0 0 10 10"><circle cx="5" cy="5" r="4.3" fill="none" stroke="#bdbdbd" stroke-width="1.2"/><path d="M0.7 5h8.6M5 0.7v8.6" stroke="#bdbdbd" stroke-width="1"/></svg>
      <span>www.velmora.cl</span>
    </li>
    <li>
      <svg viewBox="0 0 10 10"><path d="M5 0l5 5H8.5v5H6V7H4v3H1.5V5H0z"/></svg>
      <span>Av. Los Aromos Norte 418 Of. 305.<br>Providencia,<br>Santiago</span>
    </li>
  </ul>
</section>

</body>
</html>
```